Commercial Business Card - stand out, clean, simple, unique.

commercial real estate group located in Texas. Called 4 Ridges Real Estate. We want a unique yet clean and professional card. On one side I would like the 4R to be by itself or to look as unique or tasteful as possible. We have the logo in white, black, and color in case a black background or something similar looks best on one side. We need a space for our name, email, cell. website. And possibly room for a phrase or city.

Contact Information for Business Card

Name, Title, Email, Phone Number, website

```html
<!DOCTYPE html>
<html lang="en">
<head>
<meta charset="utf-8">
<title>4 Ridges Real Estate – Business Card</title>
<link rel="stylesheet" href="https://fonts.googleapis.com/css2?family=Arimo:wght@400;700&display=swap">
<style>
  :root {
    --stage: #1d1d21;
    --paper: #ffffff;
    --navy: #1f2f72;
    --navy-deep: #16235a;
    --orange: #e0793a;
    --ink-light: #ffffff;
  }
  * { box-sizing: border-box; margin: 0; padding: 0; }
  html, body {
    width: 1200px; height: 800px; overflow: hidden;
    background: var(--stage);
    font-family: "Arimo", Arial, sans-serif;
  }
  .sheet {
    width: 1200px; height: 800px;
    display: flex; flex-direction: column;
    align-items: center; justify-content: center; gap: 40px;
  }
  .card {
    position: relative;
    width: 580px; height: 331px;
    background: var(--paper);
    overflow: hidden;
  }
  .brand {
    display: flex; align-items: center; gap: 14px;
    color: var(--navy);
    font-weight: 700;
    letter-spacing: 0.06em;
    text-transform: uppercase;
  }
  .brand-dot {
    width: 30px; height: 30px; border-radius: 50%;
    background: var(--navy);
    flex: none;
  }
  .card-front .brand {
    position: absolute; left: 0; right: 0; top: 0; bottom: 0;
    justify-content: center;
    font-size: 27px;
  }
  .card-back .brand {
    position: absolute; top: 78px; left: 150px;
    font-size: 24px;
  }
  .card-back .brand-dot { width: 26px; height: 26px; }

  .name-band {
    position: absolute; left: 0; right: 0; top: 218px; height: 28px;
    background: var(--orange);
    color: var(--ink-light);
    display: flex; align-items: center; justify-content: center;
    font-size: 14px;
  }
  .person-name { font-weight: 700; letter-spacing: 0.02em; }
  .person-title { font-weight: 400; margin-left: 6px; }
  .person-title::before { content: "|"; margin-right: 6px; opacity: .8; }

  .contact-band {
    position: absolute; left: 0; right: 0; top: 246px; height: 66px;
    background: linear-gradient(180deg, var(--navy) 0%, var(--navy-deep) 100%);
    color: var(--ink-light);
    display: flex; align-items: center; justify-content: space-between;
    padding: 0 28px;
    font-size: 13px;
  }
  .contact-list, .address { list-style: none; line-height: 1.55; }
  .address { text-align: right; }
  .contact-item { display: flex; align-items: center; gap: 8px; }
  .contact-item svg { width: 12px; height: 12px; fill: var(--ink-light); flex: none; }
</style>
</head>
<body>
<main class="sheet">

  <section class="card card-front" aria-label="Card front">
    <div class="brand"><span class="brand-dot"></span>4 Ridges Real Estate</div>
  </section>

  <section class="card card-back" aria-label="Card back">
    <div class="brand"><span class="brand-dot"></span>4 Ridges Real Estate</div>

    <div class="name-band">
      <span class="person-name">DANA WHITFIELD</span>
      <span class="person-title">Director</span>
    </div>

    <div class="contact-band">
      <ul class="contact-list">
        <li class="contact-item">
          <svg viewBox="0 0 24 24" aria-hidden="true"><path d="M6.6 10.8a15.1 15.1 0 0 0 6.6 6.6l2.2-2.2a1 1 0 0 1 1-.25 11.4 11.4 0 0 0 3.6.57 1 1 0 0 1 1 1V20a1 1 0 0 1-1 1A17 17 0 0 1 3 4a1 1 0 0 1 1-1h3.5a1 1 0 0 1 1 1c0 1.25.2 2.45.57 3.57a1 1 0 0 1-.25 1z"/></svg>
          512-555-0148
        </li>
        <li class="contact-item">
          <svg viewBox="0 0 24 24" aria-hidden="true"><path d="M2 5h20v14H2z M4 7v.5l8 5 8-5V7l-8 5z" fill-rule="evenodd"/></svg>
          hello@4ridgesre.com
        </li>
      </ul>
      <ul class="address">
        <li>PO Box 418, Cedar Street</li>
        <li>Suite 2, Austin</li>
      </ul>
    </div>
  </section>

</main>
</body>
</html>
```